Beautify our company's one pager website

We need a website - currently we have only a nice light-switcher: https://brimvale.example

We got the basic contents together (see the wireframes - also in SVG format -
attached here). Now we need you (!) to make it look appealing, create proper illustrations, provide a good theme picture and advice us on how to take good employee pictures.

In the wireframes, the picture and most illustrations are just placeholders (only the logos of "Our Open Source tools" are ours - see attached logos.svg). We request you to fill all placeholders with good illustrations and make the whole page look nicely.

Only one color is pre-defined (#11233f - the blue color we use for our logo when it is on white background). Feel free to give it nice colours based on your professional expertise and intuition. Feel also free to use the blue in a more creative way, than proposed in the wireframes.

We will do the coding ourselves, but we request you to submit a responsive design, with at least one version for mobiles, one for tablet size and one for full desktop resolution.

We think our people pictures should follow a design line. Please asses us on how we should take our colleagues' pictures (e.g. completely white background, or... blurry city background, or.... with a big box in the hand, etc... we are curious to see your suggestion).

In case of any doubts, please don't hesitate to contact us (brimvale-website-design@brimvale.example).

Target Market(s)

International cooperation agencies

Industry/Entity Type

Consulting

Number of Pages Required

3 page

Font styles to use
Other font styles liked:
• Lato

Colors

Designer to choose colors to be used in the design.

Requirements
Must have
• Responsive design in mind (one pager, for three different resolutions: mobile, tablet, desktop)
• Illustrations and (maybe) a photo - must be royalty-free and open for any use in the future.
Nice to have
• SVG formated design
• Suggestions on the peoples' photos

```html
<!DOCTYPE html>
<html lang="en">
<head>
<meta charset="utf-8">
<title>Brimvale – Agile Consultancies for International Development</title>
<link href="https://fonts.googleapis.com/css2?family=Lato:wght@300;400;700&display=swap" rel="stylesheet">
<style>
:root{
  --navy:#11233f;
  --navy-deep:#0f1d36;
  --hero-top:#13335f;
  --hero-bottom:#1d5aa6;
  --blue:#2a86e0;
  --blue-text:#2b86de;
  --ink:#1d2433;
  --muted:#8a909a;
  --line:#d9dde3;
  --pale:#f4f5f8;
  --white:#ffffff;
  --footer:#eef0f3;
}
*{box-sizing:border-box;margin:0;padding:0}
html,body{width:1200px;height:3593px;overflow:hidden}
body{font-family:"Lato",Arial,sans-serif;color:var(--ink);background:var(--white);position:relative}
section,header,footer{position:absolute;left:0;width:1200px}

/* Hero */
.hero{top:0;height:563px;background:radial-gradient(ellipse at 50% 40%,#1f5497 0%,var(--hero-top) 70%);overflow:hidden}
.brand{position:absolute;left:156px;top:34px;color:var(--white);font-weight:700;font-size:26px;letter-spacing:1px}
.nav{position:absolute;left:540px;top:36px;display:flex;gap:0;align-items:center}
.nav a{color:var(--white);text-decoration:none;font-size:13px;font-weight:700;letter-spacing:1px;margin-right:42px}
.nav a.active{color:#5ea8f0}
.nav .contact-btn{margin-left:40px;border:1.5px solid #5ea8f0;border-radius:20px;padding:8px 36px;margin-right:0;font-size:12px}
.hero-title{position:absolute;top:148px;width:100%;text-align:center;color:var(--white)}
.hero-title .line1{font-size:38px;font-weight:300;display:block}
.hero-title .line2{font-size:26px;font-weight:400;display:block;margin-top:6px}
.hero-art{position:absolute;left:340px;top:250px;width:520px;height:306px;border-radius:6px;background:linear-gradient(180deg,#2a6fbf 0%,#3d7fcf 60%,#f29a6a 100%);opacity:.85}
.hero-floor{position:absolute;left:0;bottom:0;width:100%;height:8px;background:var(--blue)}

/* Intro */
.intro{top:563px;height:512px}
.intro-photo{position:absolute;left:0;top:0;width:599px;height:512px;background:linear-gradient(135deg,#4e6579 0%,#9eaab6 55%,#d7dde3 100%)}
.intro-text{position:absolute;left:685px;top:76px;width:370px}
.intro-lead{color:var(--blue-text);font-size:18px;line-height:26px}
.intro-body{color:var(--muted);font-size:13px;line-height:19px;margin-top:22px}
.btn{display:inline-block;background:var(--blue);color:var(--white);border-radius:20px;font-size:12px;font-weight:700;letter-spacing:1px;text-decoration:none;text-align:center}
.intro .btn{position:absolute;left:0;top:301px;width:130px;padding:9px 0}

/* Agile */
.agile{top:1075px;height:271px;background:var(--blue);color:var(--white)}
.agile h2{position:absolute;left:306px;top:78px;font-size:34px;font-weight:300}
.agile .rule{position:absolute;left:458px;top:100px;width:205px;height:1px;background:rgba(255,255,255,.6)}
.agile p{position:absolute;left:306px;top:130px;width:620px;font-size:13.5px;line-height:20px}
.agile p strong{font-weight:700;display:block}

/* Services */
.services{top:1346px;height:479px}
.section-title{position:absolute;width:100%;text-align:center;font-size:26px;font-weight:400;color:var(--ink)}
.services .section-title{top:76px}
.service-card{position:absolute;top:170px;width:280px;height:192px;border:1.5px solid var(--line);border-radius:3px;background:var(--white);padding:44px 30px 0}
.service-card h3{color:var(--blue-text);font-size:18px;font-weight:400;line-height:22px}
.service-card p{color:var(--muted);font-size:11.5px;line-height:16px;margin-top:14px}
.service-icon{position:absolute;left:28px;top:-38px;width:58px;height:58px;background:var(--white)}
.card-1{left:156px}.card-2{left:460px}.card-3{left:764px}
.outline-btn{position:absolute;left:535px;top:408px;width:130px;padding:8px 0;border:1.5px solid var(--line);border-radius:20px;text-align:center;font-size:11px;font-weight:700;letter-spacing:1px;color:var(--blue-text)}

/* Tools */
.tools{top:1825px;height:618px;background:var(--pale)}
.tools .section-title{top:70px}
.tools .rule{position:absolute;left:283px;width:632px;height:1px;background:var(--line)}
.tool{position:absolute;left:306px;width:600px;height:160px}
.tool-mark{position:absolute;left:0;top:8px;width:106px;height:106px;border-radius:50%}
.tool-mark.ring{border:1.5px solid var(--blue);background:var(--white)}
.tool-mark.solid{background:var(--blue)}
.tool-body{position:absolute;left:130px;top:0;width:470px}
.tool-body h3{color:var(--blue-text);font-size:19px;font-weight:400}
.tool-body p{color:var(--muted);font-size:11.5px;line-height:16px;margin-top:10px}
.tool-body .link{display:block;margin-top:14px;font-size:11px;color:var(--muted);text-decoration:underline}

/* Team */
.team{top:2443px;height:570px}
.team .section-title{top:70px}
.team .subtitle{position:absolute;top:116px;width:100%;text-align:center;color:var(--muted);font-size:13px}
.member{position:absolute;top:163px;width:204px;text-align:center}
.member .portrait{width:204px;height:223px;background:linear-gradient(180deg,#cfd2d6 0%,#8f959c 100%)}
.member.highlight .portrait{background:linear-gradient(180deg,#5a6373 0%,#2e3645 100%)}
.member h3{color:var(--blue-text);font-size:19px;font-weight:400;margin-top:22px}
.member p{color:var(--muted);font-size:11.5px;margin-top:4px}
.m1{left:156px}.m2{left:383px}.m3{left:613px}.m4{left:841px}
.arrow{position:absolute;top:265px;width:20px;height:26px}
.arrow.prev{left:96px}.arrow.next{left:1086px}
.dots{position:absolute;top:478px;left:580px;display:flex;gap:8px}
.dots span{width:9px;height:9px;border-radius:50%;border:1px solid var(--muted)}
.dots span.on{background:var(--ink);border-color:var(--ink)}

/* Contact */
.contact{top:3013px;height:503px}
.contact-panel{position:absolute;left:0;top:0;width:600px;height:503px;background:var(--navy)}
.contact-panel h2{position:absolute;left:156px;top:78px;color:var(--white);font-size:27px;font-weight:400}
.contact-panel .subtitle{position:absolute;left:156px;top:118px;color:#9aa6b8;font-size:12.5px}
.field{position:absolute;left:156px;width:354px;border:1px solid #4a5c7a;border-radius:2px;color:#8c99ae;font-size:11.5px;padding:9px 12px}
.f-name{top:158px;height:34px}
.f-email{top:206px;height:34px}
.f-message{top:254px;height:115px}
.contact .btn{position:absolute;left:156px;top:400px;width:127px;padding:10px 0}
.map{position:absolute;left:600px;top:0;width:600px;height:503px;background:linear-gradient(135deg,#e4e4e4 0%,#cfcfcf 100%)}

/* Footer */
.site-footer{top:3516px;height:77px;background:var(--footer);font-size:11.5px;color:var(--muted)}
.site-footer .address{position:absolute;left:156px;top:38px;display:flex;align-items:center;gap:8px}
.site-footer .address-2{position:absolute;left:611px;top:38px}
.site-footer .imprint{position:absolute;left:988px;top:38px;color:var(--blue-text);text-decoration:underline}
</style>
</head>
<body>

<header class="hero">
  <div class="brand">Brimvale</div>
  <nav class="nav">
    <a class="active" href="#about">ABOUT</a>
    <a href="#services">SERVICES</a>
    <a href="#tools">TOOLS</a>
    <a href="#team">TEAM</a>
    <a class="contact-btn" href="#contact">CONTACT</a>
  </nav>
  <h1 class="hero-title"><span class="line1">Agile Consultancies for</span><span class="line2">International Development</span></h1>
  <div class="hero-art" role="img" aria-label="Illustration of a cheerful consultant working at a laptop beside a desk lamp, wall clock and printer"></div>
  <div class="hero-floor"></div>
</header>

<section class="intro" id="about">
  <div class="intro-photo" role="img" aria-label="Photo of business people reviewing charts on a tablet at a desk"></div>
  <div class="intro-text">
    <p class="intro-lead">Brimvale provides institutions working in the international cooperation field (implementing agencies, local gvernmental and non-governmental institutions) with solutions (hardware, software and consultancy services)</p>
    <p class="intro-body">to better organize, manage and exchange their knowledge in form of data and information (knowledge management).</p>
    <a class="btn" href="#about">ABOUT US</a>
  </div>
</section>

<section class="agile">
  <h2>Agile</h2>
  <div class="rule"></div>
  <p><strong>Efficient and flexible methodology for developing successful solutions with fun.</strong>Is is based on iterative, measurable and verifiable small steps, with integrative and empowering involvement of all actors.</p>
</section>

<section class="services" id="services">
  <h2 class="section-title">Service We offer</h2>

  <article class="service-card card-1">
    <svg class="service-icon" viewBox="0 0 58 58" aria-hidden="true">
      <rect x="8" y="12" width="42" height="28" rx="2" fill="none" stroke="#2a86e0" stroke-width="2"/>
      <line x1="22" y1="46" x2="36" y2="46" stroke="#2a86e0" stroke-width="2"/>
      <line x1="29" y1="40" x2="29" y2="46" stroke="#2a86e0" stroke-width="2"/>
      <line x1="14" y1="20" x2="30" y2="20" stroke="#2a86e0" stroke-width="2"/>
      <line x1="14" y1="26" x2="40" y2="26" stroke="#2a86e0" stroke-width="2"/>
    </svg>
    <h3>Technology<br>for International Aid</h3>
    <p>Meaningful implementation and application of Digital Media, Software and Hardware with a sensibility for the world.</p>
  </article>

  <article class="service-card card-2">
    <svg class="service-icon" viewBox="0 0 58 58" aria-hidden="true">
      <rect x="8" y="36" width="7" height="12" fill="none" stroke="#2a86e0" stroke-width="2"/>
      <rect x="20" y="30" width="7" height="18" fill="none" stroke="#2a86e0" stroke-width="2"/>
      <rect x="32" y="24" width="7" height="24" fill="none" stroke="#2a86e0" stroke-width="2"/>
      <rect x="44" y="18" width="7" height="30" fill="none" stroke="#2a86e0" stroke-width="2"/>
      <polyline points="8,28 22,20 32,16 48,6" fill="none" stroke="#2a86e0" stroke-width="2"/>
      <polyline points="42,6 48,6 48,12" fill="none" stroke="#2a86e0" stroke-width="2"/>
    </svg>
    <h3>Organizational<br>Development</h3>
    <p>Agile and data-driven approach to accompany organizations into change processes.</p>
  </article>

  <article class="service-card card-3">
    <svg class="service-icon" viewBox="0 0 58 58" aria-hidden="true">
      <rect x="22" y="6" width="14" height="10" fill="none" stroke="#2a86e0" stroke-width="2"/>
      <rect x="6" y="40" width="14" height="10" fill="none" stroke="#2a86e0" stroke-width="2"/>
      <rect x="22" y="40" width="14" height="10" fill="none" stroke="#2a86e0" stroke-width="2"/>
      <rect x="38" y="40" width="14" height="10" fill="none" stroke="#2a86e0" stroke-width="2"/>
      <polyline points="29,16 29,28 13,28 13,40" fill="none" stroke="#2a86e0" stroke-width="2"/>
      <polyline points="29,28 45,28 45,40" fill="none" stroke="#2a86e0" stroke-width="2"/>
      <line x1="29" y1="28" x2="29" y2="40" stroke="#2a86e0" stroke-width="2"/>
    </svg>
    <h3>Data and Knowledge<br>Management</h3>
    <p>Needs assessment, organizational and requirement analysis for ICT-based support to knowledge processes in communities of practice.</p>
  </article>

  <div class="outline-btn">CONSULT NOW</div>
</section>

<section class="tools" id="tools">
  <h2 class="section-title">Our Open Source tools</h2>
  <div class="rule" style="top:139px"></div>

  <article class="tool" style="top:182px">
    <div class="tool-mark ring"></div>
    <div class="tool-body">
      <h3>D-Vault</h3>
      <p>Open Source web-based document management system. This Software allows organizations and groups to flexibly manage their knowledge through documents and data. The files can be structured and access can be managed for groups of people or for specific persons.</p>
      <a class="link" href="#tools">https://code.brimvale.example/d-vault</a>
    </div>
  </article>

  <article class="tool" style="top:378px">
    <div class="tool-mark solid"></div>
    <div class="tool-body">
      <h3>D-Mesh</h3>
      <p>Several decentralized D-Vaults can be connected over a D-Mesh. This allows to manage data over different instances and create organizational partnerships for networks of providing access to information and enhance knowledge in the developing world.</p>
      <a class="link" href="#tools">https://code.brimvale.example/d-mesh</a>
    </div>
  </article>

  <div class="rule" style="top:534px"></div>
</section>

<section class="team" id="team">
  <h2 class="section-title">Our Team</h2>
  <p class="subtitle">We are cultural technologists</p>

  <svg class="arrow prev" viewBox="0 0 20 26" aria-hidden="true"><polyline points="14,3 5,13 14,23" fill="none" stroke="#c3c7cd" stroke-width="2"/></svg>
  <svg class="arrow next" viewBox="0 0 20 26" aria-hidden="true"><polyline points="6,3 15,13 6,23" fill="none" stroke="#c3c7cd" stroke-width="2"/></svg>

  <div class="member m1">
    <div class="portrait" role="img" aria-label="Portrait photo of a team member in a suit on a light grey background"></div>
    <h3>Dr. Marco Selvani</h3>
    <p>Chief Executive Officer</p>
  </div>
  <div class="member m2 highlight">
    <div class="portrait" role="img" aria-label="Portrait photo of a team member on a dark grey background"></div>
    <h3>Irena Volkers</h3>
    <p>Chief Executive Officer</p>
  </div>
  <div class="member m3">
    <div class="portrait" role="img" aria-label="Portrait photo of a smiling team member on a light grey background"></div>
    <h3>Jonas Perrault</h3>
    <p>Digital Product manager</p>
  </div>
  <div class="member m4">
    <div class="portrait" role="img" aria-label="Portrait photo of a team member in a blue shirt on a light grey background"></div>
    <h3>Luca Ferrandi</h3>
    <p>Lead developer</p>
  </div>

  <div class="dots"><span></span><span class="on"></span><span></span></div>
</section>

<section class="contact" id="contact">
  <div class="contact-panel">
    <h2>Contact Us</h2>
    <p class="subtitle">Write and visit us</p>
    <div class="field f-name">Your Name</div>
    <div class="field f-email">Email</div>
    <div class="field f-message">Type your Message</div>
    <a class="btn" href="#contact">SEND</a>
  </div>
  <div class="map" role="img" aria-label="Greyscale city map with a location pin marking the office"></div>
</section>

<footer class="site-footer">
  <div class="address">
    <svg width="10" height="14" viewBox="0 0 10 14" aria-hidden="true"><path d="M5 0C2.2 0 0 2.2 0 5c0 3.7 5 9 5 9s5-5.3 5-9C10 2.2 7.8 0 5 0zm0 7a2 2 0 1 1 0-4 2 2 0 0 1 0 4z" fill="#8a909a"/></svg>
    <span>Brimvale UG Harbour Lane 14, 40210 Eastmoor</span>
  </div>
  <div class="address-2">To be defined street Northbay, Westland</div>
  <a class="imprint" href="#contact">Impressum</a>
</footer>

</body>
</html>
```